Design a powerpoint background using company logo/colours

We require a powerpoint background that incorporates our company colours and logo. I have attached the logo in various sizes.

Have fun and be imaginative

Our company colours are white and Red-236, Green-22 and Blue 86.
Please use these colours in designing the ppt background

Industry/Entity Type

It Company

Colors

Designer to choose colors to be used in the design.

```html
<!DOCTYPE html>
<html lang="en">
<head>
<meta charset="utf-8">
<title>Slide Background</title>
<link rel="stylesheet" href="https://fonts.googleapis.com/css2?family=Arimo:ital,wght@0,400;0,700;1,400&display=swap">
<style>
  :root {
    --brand: #ec1656;
    --white: #ffffff;
    --ink: #333333;
    --muted: #555555;
    --backdrop-top: #e6e7e9;
    --backdrop-mid: #eeeff0;
    --backdrop-bottom: #fbfbfb;
    --backdrop-shade: rgba(200, 202, 206, 0.55);
  }
  * { margin: 0; padding: 0; box-sizing: border-box; }
  html, body { width: 1200px; height: 900px; overflow: hidden; background: var(--white); }
  body { font-family: "Arimo", Arial, sans-serif; }
  .slide { position: relative; width: 1200px; height: 900px; background: var(--white); overflow: hidden; }

  .top-band { position: absolute; left: 0; top: 0; width: 1200px; height: 30px; background: var(--brand); }

  .header { position: absolute; left: 0; top: 30px; width: 1200px; height: 130px; background: var(--white); }
  .brand { position: absolute; left: 46px; top: 26px; }
  .brand-row { display: flex; align-items: center; gap: 14px; }
  .brand-name { font-size: 56px; font-weight: 700; color: var(--brand); letter-spacing: 1px; line-height: 1; }
  .brand-mark { width: 22px; height: 22px; background: var(--brand); }
  .brand-tagline { margin-top: 8px; font-size: 15px; color: var(--muted); line-height: 1; }

  .slide-meta { position: absolute; right: 44px; top: 25px; text-align: right; color: var(--ink); font-size: 17px; line-height: 21px; }

  .backdrop {
    position: absolute; left: 0; top: 160px; width: 1200px; height: 680px;
    background:
      radial-gradient(ellipse 420px 620px at 600px 40px, var(--backdrop-shade) 0%, rgba(200,202,206,0.25) 55%, rgba(200,202,206,0) 100%),
      linear-gradient(180deg, var(--backdrop-top) 0%, var(--backdrop-mid) 50%, var(--backdrop-bottom) 100%);
  }

  .footer-band { position: absolute; left: 0; top: 840px; width: 1200px; height: 30px; background: var(--brand); }
  .footer-text { position: absolute; top: 848px; color: var(--white); font-size: 13px; line-height: 14px; white-space: nowrap; }
  .copyright { left: 46px; }
  .presenter { left: 323px; }
  .footer-divider { position: absolute; left: 297px; top: 840px; width: 1px; height: 60px; background: var(--brand); }
  .footer-divider-light { position: absolute; left: 297px; top: 840px; width: 1px; height: 30px; background: rgba(255,255,255,0.6); }
  .page-number {
    position: absolute; left: 1122px; top: 838px; width: 33px; height: 33px;
    background: var(--white); border: 1px solid var(--brand); color: var(--brand);
    font-size: 16px; display: flex; align-items: center; justify-content: center;
  }
</style>
</head>
<body>
<div class="slide">
  <div class="top-band"></div>
  <header class="header">
    <div class="brand">
      <div class="brand-row">
        <span class="brand-name">NEXORA</span>
        <span class="brand-mark"></span>
      </div>
    </div>
    <div class="slide-meta">
      <div class="slide-title">PRESENTATION TITLE</div>
      <div class="slide-date">DATE</div>
    </div>
  </header>
  <div class="backdrop" role="img" aria-label="Faded full-width photograph of a steel lattice telecommunications tower seen from below, rising to a point against a pale misty sky"></div>
  <footer>
    <div class="footer-band"></div>
    <div class="footer-divider"></div>
    <div class="footer-divider-light"></div>
    <span class="footer-text copyright">Copyright © 2014 Nexora Group Pty Ltd</span>
    <span class="footer-text presenter">Presenting by DANIEL MORROW</span>
    <div class="page-number">2</div>
  </footer>
</div>
</body>
</html>
```